New Business Card Design Project

We are looking for a talented individual to create a truly awesome/unique business card design for us. We are looking for a someone to design something that will really stand out from the crowd - we don't mind what ideas you come up with (ie embossed/flat/matte/shine etc etc) just wow us with your creativity.
Updates

Sick

Target Market(s)

Video Games Industry Professionals (all levels of seniority from QA Testers through to CEOs)

Contact Information for Business Card

Company logo (see upload)
Company name: Northbridge Play Careers Ltd
Employee Name: Harriet Vasko
Job title: CEO
Website: www.npc2go.com
Office +44 1632 960418
Mobile: +44 7700 900582
Email: harriet@npc2go.com

Colors

Designer to choose colors to be used in the design.

Requirements
Must have
• The business card design MUST contain all the information listed in the BUSINESS CARD DETAILS box.
• You will see the colours that are relevant to us (ie company logo) in the uploaded imagery - however you do not have to use all these colours when designing the business card itself
• MUST BE DOUBLE SIDED

```html
<!DOCTYPE html>
<html lang="en">
<head>
<meta charset="utf-8">
<title>Northbridge Play Careers – Business Card</title>
<link rel="stylesheet" href="https://fonts.googleapis.com/css2?family=Montserrat:wght@600;700&family=Open+Sans:wght@400;600&display=swap">
<style>
  :root {
    --bg: #2b2b2b;
    --card: #1f1f1f;
    --card-edge: #262626;
    --orange: #f07d1a;
    --text: #e8e8e8;
    --muted: #8a8a8a;
    --rule: #9a9a9a;
  }
  * { margin: 0; padding: 0; box-sizing: border-box; }
  html, body { width: 1200px; height: 895px; overflow: hidden; }
  body {
    background: var(--bg);
    font-family: "Open Sans", sans-serif;
    position: relative;
  }
  .card {
    position: absolute;
    width: 620px;
    height: 354px;
    background: linear-gradient(160deg, var(--card-edge), var(--card));
    box-shadow: 0 14px 30px rgba(0,0,0,0.55);
    overflow: hidden;
  }
  .card--front { left: 70px; top: 70px; }
  .card--back { left: 510px; top: 470px; }

  /* front side */
  .front-mark {
    position: absolute;
    left: 70px; top: 117px;
    display: flex; align-items: center; gap: 22px;
  }
  .front-mark__dot {
    width: 110px; height: 110px; border-radius: 50%;
    background: #2a2a2a;
  }
  .front-mark__name {
    font-family: "Montserrat", sans-serif;
    font-weight: 700;
    font-size: 34px;
    line-height: 1.05;
    color: #9c9c9c;
    letter-spacing: 0.5px;
  }

  /* back side */
  .brand {
    position: absolute;
    right: 46px; top: 44px;
    display: flex; align-items: center; gap: 14px;
  }
  .brand__dot {
    width: 58px; height: 58px; border-radius: 50%;
    background: #2c3a78;
  }
  .brand__name {
    font-family: "Montserrat", sans-serif;
    font-weight: 700;
    font-size: 22px;
    line-height: 1.1;
    color: var(--text);
  }
  .divider {
    position: absolute;
    left: 36px; right: 36px;
    height: 1px;
    background: var(--rule);
  }
  .divider--top { top: 148px; left: 300px; }
  .person {
    position: absolute;
    left: 36px; top: 170px;
  }
  .person__line { display: flex; align-items: baseline; gap: 12px; }
  .person__name {
    font-family: "Montserrat", sans-serif;
    font-weight: 600;
    font-size: 30px;
    color: var(--orange);
  }
  .person__sep { width: 2px; height: 24px; background: var(--text); align-self: center; }
  .person__title {
    font-family: "Montserrat", sans-serif;
    font-weight: 600;
    font-size: 16px;
    color: var(--text);
  }
  .person__company { font-size: 15px; color: var(--text); margin-top: 2px; }
  .divider--mid { top: 250px; width: 230px; right: auto; }
  .contacts {
    position: absolute;
    left: 36px; top: 262px;
    list-style: none;
  }
  .contacts li {
    display: flex; align-items: center; gap: 12px;
    font-size: 15px; color: var(--text);
    height: 26px;
  }
  .contacts svg { width: 14px; height: 14px; flex: none; }
  .website {
    position: absolute;
    right: 24px; bottom: 46px;
    font-size: 14px; color: var(--text);
  }
  .website-bar {
    position: absolute;
    right: 24px; bottom: 32px;
    width: 130px; height: 5px;
    background: var(--orange);
  }
</style>
</head>
<body>
  <section class="card card--front" aria-label="Business card front">
    <div class="front-mark">
      <span class="front-mark__dot"></span>
      <span class="front-mark__name">Northbridge<br>Play Careers</span>
    </div>
  </section>

  <section class="card card--back" aria-label="Business card back">
    <div class="brand">
      <span class="brand__dot"></span>
      <span class="brand__name">Northbridge<br>Play Careers</span>
    </div>
    <div class="divider divider--top"></div>

    <div class="person">
      <div class="person__line">
        <span class="person__name">Harriet Vasko</span>
        <span class="person__sep"></span>
        <span class="person__title">CEO</span>
      </div>
      <div class="person__company">Northbridge Play Careers Ltd</div>
    </div>
    <div class="divider divider--mid"></div>

    <ul class="contacts">
      <li>
        <svg viewBox="0 0 14 14" aria-hidden="true"><rect x="3.5" y="1" width="7" height="12" rx="1.2" fill="none" stroke="#f07d1a" stroke-width="1.4"/><circle cx="7" cy="11" r="0.8" fill="#f07d1a"/></svg>
        +44 7700 900582
      </li>
      <li>
        <svg viewBox="0 0 14 14" aria-hidden="true"><path d="M3 1.5l2.2 2.6-1.2 1.5c.9 1.8 2.3 3.2 4.1 4.1l1.5-1.2 2.6 2.2-1.4 1.8C5.9 12.3 1.7 8.1 1.2 3z" fill="#f07d1a"/></svg>
        +44 1632 960418
      </li>
      <li>
        <svg viewBox="0 0 14 14" aria-hidden="true"><rect x="1" y="3" width="12" height="9" fill="#f07d1a"/><path d="M1 3l6 5 6-5" fill="none" stroke="#1f1f1f" stroke-width="1.2"/></svg>
        harriet@npc2go.com
      </li>
    </ul>

    <div class="website">www.npc2go.com</div>
    <div class="website-bar"></div>
  </section>
</body>
</html>
```